TAMBERLY DISTRIBUTION VAN SIGNAGE

We would like a design done for our range of vans: the first van to be wrapped/logo'd will be a light grey corvane hauler if you wish to use this as template van. I have included our company logo( we do not need this redesigned) We like the design to be simple yet modern and funky. We need the Tamberly logo to be prominant. Other Details to include:

The phone number: +442847751932
Email: info@tamberly-example.eu.
Website: www.tamberly-example.eu

Target Market(s)

Retail stores

Font styles to use
Sans Serif

```html
<!DOCTYPE html>
<html lang="en">
<head>
<meta charset="utf-8">
<title>Tamberly Distribution – Van Signage</title>
<link rel="stylesheet" href="https://fonts.googleapis.com/css2?family=Josefin+Sans:wght@300;400;600;700&display=swap">
<style>
  :root {
    --page: #ffffff;
    --body: #4a4a4d;
    --panel-dark: #2f2f32;
    --panel-mid: #3b3b3e;
    --glass: #d9dcdf;
    --trim: #1f1f21;
    --tyre: #1b1b1c;
    --rim: #c3c6c9;
    --silver: #e4e6e8;
    --ink: #ffffff;
    --lamp: #8e1c22;
  }
  html, body {
    margin: 0;
    width: 1200px;
    height: 1200px;
    overflow: hidden;
    background: var(--page);
  }
  .canvas { display: block; width: 1200px; height: 1200px; }
  .van-body { fill: var(--body); }
  .panel-dark { fill: var(--panel-dark); }
  .panel-mid { fill: var(--panel-mid); }
  .window { fill: var(--glass); }
  .trim { fill: var(--trim); }
  .tyre { fill: var(--tyre); }
  .rim { fill: var(--rim); }
  .hub { fill: #8d9195; }
  .tail-lamp { fill: var(--lamp); }
  .door-line { stroke: #2a2a2c; stroke-width: 1.2; fill: none; }
  .brand-ring { fill: none; stroke: var(--silver); stroke-width: 9; }
  .brand-name, .brand-sub, .contact {
    font-family: "Josefin Sans", sans-serif;
    fill: var(--ink);
  }
  .brand-name { font-weight: 600; }
  .brand-sub { font-weight: 300; }
  .contact { font-weight: 700; }
  .contact-light { font-weight: 400; }
  .shadow { fill: #e8e8e8; }
</style>
</head>
<body>
<svg class="canvas" viewBox="0 0 960 960" xmlns="http://www.w3.org/2000/svg" role="img" aria-label="Tamberly Distribution van signage, two side layouts">
  <defs>
    <path id="van-shape" d="M90 262 L160 222 L268 138 Q280 128 300 128 L860 124 Q878 124 880 140 L884 388 Q884 402 870 402 L76 404 Q62 404 60 390 L58 300 Q60 272 90 262 Z"/>
    <clipPath id="van-clip"><use href="#van-shape"/></clipPath>
  </defs>

  <!-- Layout one -->
  <g class="van van-one">
    <ellipse class="shadow" cx="480" cy="412" rx="420" ry="10"/>
    <use href="#van-shape" class="van-body"/>
    <g clip-path="url(#van-clip)">
      <polygon class="panel-mid" points="40,330 520,130 900,130 900,420 40,420"/>
      <polygon class="panel-dark" points="460,120 900,120 900,420 700,420 560,300"/>
      <rect class="trim" x="40" y="360" width="860" height="50"/>
    </g>
    <polygon class="window" points="300,148 440,144 442,240 248,240"/>
    <path class="door-line" d="M445 140 L448 398 M660 130 L662 398"/>
    <rect class="tail-lamp" x="872" y="240" width="10" height="40" rx="3"/>
    <g class="wheel"><circle class="tyre" cx="200" cy="388" r="50"/><circle class="rim" cx="200" cy="388" r="34"/><circle class="hub" cx="200" cy="388" r="8"/></g>
    <g class="wheel"><circle class="tyre" cx="770" cy="388" r="50"/><circle class="rim" cx="770" cy="388" r="34"/><circle class="hub" cx="770" cy="388" r="8"/></g>

    <circle class="brand-ring" cx="570" cy="248" r="112"/>
    <text class="brand-name" x="685" y="200" font-size="24" letter-spacing="2">TAMBERLY</text>
    <text class="brand-sub" x="688" y="224" font-size="11" letter-spacing="2.5">DISTRIBUTION</text>
    <text class="contact" x="708" y="276" font-size="12" letter-spacing="0.6">info@tamberly-example.eu</text>
    <text class="contact" x="278" y="299" font-size="15" letter-spacing="0.8">+44 28 47 751932</text>
    <text class="contact contact-light" x="278" y="318" font-size="13" letter-spacing="1.2">www.tamberly-example.eu</text>
  </g>

  <!-- Layout two -->
  <g class="van van-two" transform="translate(0 370)">
    <ellipse class="shadow" cx="480" cy="412" rx="420" ry="10"/>
    <use href="#van-shape" class="van-body"/>
    <g clip-path="url(#van-clip)">
      <polygon class="panel-dark" points="250,405 900,150 900,300 440,420 250,420"/>
      <polygon class="panel-mid" points="600,120 900,120 900,150 560,290 470,290"/>
      <rect class="trim" x="40" y="370" width="860" height="40"/>
    </g>
    <polygon class="window" points="300,148 440,144 442,240 248,240"/>
    <path class="door-line" d="M445 140 L448 398 M660 130 L662 398"/>
    <rect class="tail-lamp" x="872" y="240" width="10" height="40" rx="3"/>
    <g class="wheel"><circle class="tyre" cx="200" cy="388" r="50"/><circle class="rim" cx="200" cy="388" r="34"/><circle class="hub" cx="200" cy="388" r="8"/></g>
    <g class="wheel"><circle class="tyre" cx="770" cy="388" r="50"/><circle class="rim" cx="770" cy="388" r="34"/><circle class="hub" cx="770" cy="388" r="8"/></g>

    <circle class="brand-ring" cx="375" cy="318" r="58" stroke-width="7"/>
    <g transform="rotate(-19 462 300)">
      <text class="brand-name" x="462" y="300" font-size="46" letter-spacing="4" textLength="395">TAMBERLY</text>
      <text class="brand-sub" x="474" y="336" font-size="21" letter-spacing="5" textLength="255">DISTRIBUTION</text>
      <text class="contact" x="478" y="374" font-size="13" letter-spacing="0.8">+44 28 47 751932  |  <tspan class="contact-light">www.tamberly-example.eu</tspan></text>
    </g>
  </g>
</svg>
</body>
</html>
```